Podcast Cover Art for Fast Growing Show (Ill include a gracious tip!)

This artwork is for "The Steadfast Fellow Hour." The podcast is for men, and it's all about self-improvement, confidence, success, money, women and masculinity. It's for the guy who wants to improve himself. I'd like for my picture to be included — in black and white — and I want the text to read: "The Steadfast Fellow Hour" and somewhere in there it'll say: "with Dale Horvik." I'm open to color schemes. The podcast is a little edgy so I'd like for that to be represented in the design. Thank you! (((Here's the podcast page if you wanna check it out: http://steadfastfellowhour.castvane.example/)))

Target Market(s)

Men who want to attract women and improve their lives!

Font styles to use
Serif

Colors

Designer to choose colors to be used in the design.

Requirements
Must have
• My image in it (in black and white) and the two titles: "The Steadfast Fellow Hour" and "with Dale Horvik"
Nice to have
• My logo in it somehow (which is the arrow looking logo attached below). I've also found that my image looks best in black and white and with a circular type cut out (although I'm open to different design ideas). I've attached my logo with a circular cut out below so you can see what I'm talking about.
Should not have
• Flowers. Teddy bears. ice cream.

```html
<!DOCTYPE html>
<html lang="en">
<head>
<meta charset="utf-8">
<title>The Steadfast Fellow Hour</title>
<link rel="stylesheet" href="https://fonts.googleapis.com/css2?family=Arimo:wght@400;700&family=Open+Sans:wght@400;700&family=Tinos&display=swap">
<style>
:root{
  --ink:#000;
  --paper:#fff;
  --link:#337ab7;
  --body-text:#333;
  --muted:#777;
  --rule:#ddd;
  --red-deep:#7a3d42;
  --red-mid:#b5464a;
  --red-soft:#d07a7a;
  --track:#e6e6e6;
}
*{box-sizing:border-box;margin:0;padding:0}
html,body{width:1200px;height:960px;overflow:hidden;background:var(--paper)}
body{position:relative;font-family:"Arimo",Arial,sans-serif;color:var(--body-text)}
.abs{position:absolute}

/* top navigation */
.site-nav{left:0;top:0;width:1200px;height:52px;background:var(--ink);border-bottom:1px solid #ccc;z-index:3}
.search-field{left:793px;top:10px;width:180px;height:33px;background:var(--paper);border:1px solid #ccc;border-radius:4px;font-size:14px;color:#999;padding:8px 12px}
.search-button{left:980px;top:10px;width:36px;height:33px;background:var(--paper);border-radius:4px;display:flex;align-items:center;justify-content:center}
.nav-link{top:17px;font-size:15px;color:var(--paper)}
.nav-about{left:1031px}
.nav-episodes{left:1097px}

.brand-mark{left:27px;top:16px;width:80px;height:80px;background:var(--paper);z-index:4;display:flex;flex-direction:column;align-items:center;justify-content:center;gap:4px;padding:4px}
.brand-mark .dot{width:12px;height:12px;background:var(--red-mid)}
.brand-mark span{font-family:"Tinos",serif;font-size:11px;line-height:12px;color:var(--ink);text-align:center}

/* hero */
.hero{left:0;top:52px;width:1200px;height:499px;overflow:hidden}
.hero-backdrop{left:0;top:0;width:1200px;height:499px;background:linear-gradient(120deg,var(--red-soft) 0%,var(--red-mid) 35%,var(--red-deep) 60%,var(--red-mid) 100%)}
.host-portrait{left:420px;top:0;width:780px;height:499px}
.show-title{left:24px;top:179px;width:513px;height:67px;background:var(--ink);color:var(--paper);font-family:"Tinos",serif;font-weight:400;font-size:47px;line-height:67px;padding-left:22px;white-space:nowrap}
.show-subtitle{left:48px;top:252px;font-family:"Tinos",serif;font-size:46px;color:var(--paper);letter-spacing:44px}
.host-credit{right:26px;top:196px;width:260px;text-align:right;font-family:"Tinos",serif}
.host-with{display:block;font-size:20px;line-height:24px;color:var(--ink);letter-spacing:15px;margin-right:14px}
.host-name{display:block;font-size:38px;line-height:40px;color:var(--paper);white-space:nowrap}
.hero-name-tag{right:26px;top:14px;font-family:"Tinos",serif;font-size:14px;color:var(--ink);text-align:right;line-height:16px}

/* subscribe bar */
.subscribe-bar{left:27px;top:562px;width:1140px;height:74px;background:var(--ink);border-radius:4px;border:1px solid #5ac}
.subscribe-btn{top:14px;width:44px;height:34px;background:var(--paper);border-radius:4px;display:flex;align-items:center;justify-content:center}

/* episodes */
.episode-title{left:42px;font-size:20px;font-weight:700;color:var(--link);white-space:nowrap}
.episode-date{left:612px;font-size:13px;color:var(--muted)}
.episode-summary{left:612px;width:530px;font-size:14px;line-height:20px;color:var(--body-text)}
.read-more{left:1056px;font-size:15px;color:var(--link)}
.episode-rule{left:125px;width:945px;height:1px;background:var(--rule)}

.player{left:42px;width:540px;height:90px;font-family:"Open Sans",sans-serif}
.player-art{left:0;top:0;width:90px;height:90px;background:var(--ink);color:var(--paper);font-family:"Tinos",serif;font-size:11px;line-height:13px;display:flex;align-items:center;justify-content:center;text-align:center;padding:6px}
.player-play{left:93px;top:0;width:81px;height:64px;border:1px solid var(--rule);display:flex;align-items:center;justify-content:center}
.player-show{left:178px;top:2px;font-size:11px;color:var(--muted);text-transform:uppercase}
.player-episode{left:178px;top:16px;font-size:12.5px;font-weight:700;color:var(--ink);white-space:nowrap}
.player-track{left:178px;top:35px;width:362px;height:22px;background:var(--track)}
.player-controls{left:93px;top:64px;width:447px;height:26px;border:1px solid var(--rule);border-top:none;font-size:13px;color:var(--ink)}
.player-controls span{position:absolute;top:5px}
.player-controls .divider{top:0;width:1px;height:25px;background:var(--rule)}
.player-controls svg{position:absolute;top:5px}
</style>
</head>
<body>

<header class="site-nav abs">
  <div class="search-field abs">Search</div>
  <div class="search-button abs">
    <svg width="14" height="14" viewBox="0 0 14 14"><circle cx="5.8" cy="5.8" r="4.3" fill="none" stroke="#000" stroke-width="2"/><line x1="9" y1="9" x2="13" y2="13" stroke="#000" stroke-width="2.4"/></svg>
  </div>
  <span class="nav-link nav-about abs">About</span>
  <span class="nav-link nav-episodes abs">Episodes &#9662;</span>
</header>

<div class="brand-mark abs"><div class="dot"></div><span>The Steadfast Fellow Hour</span></div>

<section class="hero abs">
  <div class="hero-backdrop abs" role="img" aria-label="Red camouflage pattern background"></div>
  <svg class="host-portrait abs" viewBox="0 0 780 499" role="img" aria-label="Black and white portrait of host Dale Horvik with hands steepled">
    <defs>
      <linearGradient id="portraitTone" x1="0" y1="0" x2="0" y2="1">
        <stop offset="0" stop-color="#9a9a9a"/>
        <stop offset="0.45" stop-color="#6a6a6a"/>
        <stop offset="1" stop-color="#2a2a2a"/>
      </linearGradient>
    </defs>
    <path d="M228 0 L226 22 L214 46 L220 74 L206 92 L210 120 L196 150 L184 188 L170 210 L152 260 L122 300 L96 360 L60 400 L30 450 L0 499 L780 499 L780 432 L758 420 L720 412 L692 370 L660 340 L640 300 L600 270 L596 228 L578 196 L560 176 L548 140 L540 100 L528 70 L520 40 L516 0 Z" fill="#f4f4f4"/>
    <path d="M248 0 L244 30 L234 60 L238 86 L226 110 L226 140 L212 176 L196 210 L172 260 L142 304 L116 362 L80 406 L50 456 L24 499 L780 499 L780 452 L740 436 L702 422 L672 384 L642 352 L620 310 L582 282 L574 236 L556 202 L536 180 L524 144 L518 104 L504 70 L498 36 L494 0 Z" fill="url(#portraitTone)"/>
  </svg>
  <div class="hero-name-tag abs">The Steadfast<br>Fellow Hour</div>
  <h1 class="show-title abs">The Steadfast Fellow</h1>
  <div class="show-subtitle abs">Hour</div>
  <div class="host-credit abs">
    <span class="host-with">with</span>
    <span class="host-name">Dale Horvik</span>
  </div>
</section>

<nav class="subscribe-bar abs">
  <div class="subscribe-btn abs" style="left:535px">
    <svg width="14" height="11" viewBox="0 0 14 11"><rect x="0" y="0" width="14" height="11" rx="1.5" fill="#333"/><path d="M1 1.5 L7 6 L13 1.5" fill="none" stroke="#fff" stroke-width="1.2"/></svg>
  </div>
  <div class="subscribe-btn abs" style="left:584px">
    <svg width="12" height="12" viewBox="0 0 12 12"><circle cx="2" cy="10" r="1.6" fill="#333"/><path d="M1 5.5 A5.5 5.5 0 0 1 6.5 11" fill="none" stroke="#333" stroke-width="1.8"/><path d="M1 1 A10 10 0 0 1 11 11" fill="none" stroke="#333" stroke-width="1.8"/></svg>
  </div>
</nav>

<h2 class="episode-title abs" style="top:662px">How You're KILLING Your TESTOSTERONE!</h2>
<div class="player abs" style="top:709px">
  <div class="player-art abs">The Steadfast Fellow Hour</div>
  <div class="player-play abs"><svg width="26" height="30" viewBox="0 0 26 30"><path d="M1 0 L26 15 L1 30 Z" fill="#000"/></svg></div>
  <div class="player-show abs">The Steadfast Fellow Hour</div>
  <div class="player-episode abs">How You're KILLING Your TESTOSTERONE!</div>
  <div class="player-track abs"></div>
  <div class="player-controls abs">
    <span style="left:33px">30&#8630;</span>
    <span style="left:85px">00:00:00</span>
    <span style="left:177px">&#8631;30</span>
    <div class="divider abs" style="left:224px"></div>
    <svg style="left:248px" width="14" height="14" viewBox="0 0 12 12"><circle cx="2" cy="10" r="1.4" fill="#333"/><path d="M1 5.5 A5.5 5.5 0 0 1 6.5 11 M1 1 A10 10 0 0 1 11 11" fill="none" stroke="#333" stroke-width="1.2"/></svg>
    <svg style="left:300px" width="16" height="16" viewBox="0 0 16 16"><path d="M8 1 V11 M4 7 L8 11 L12 7 M2 12 V15 H14 V12" fill="none" stroke="#333" stroke-width="1.3"/></svg>
    <svg style="left:353px" width="20" height="16" viewBox="0 0 20 16"><path d="M6 3 L1 8 L6 13 M14 3 L19 8 L14 13 M12 1 L8 15" fill="none" stroke="#333" stroke-width="1.4"/></svg>
    <svg style="left:407px" width="18" height="16" viewBox="0 0 18 16"><circle cx="9" cy="3" r="2.2" fill="none" stroke="#333" stroke-width="1.2"/><circle cx="3" cy="12" r="2.2" fill="none" stroke="#333" stroke-width="1.2"/><circle cx="15" cy="12" r="2.2" fill="none" stroke="#333" stroke-width="1.2"/><path d="M7.5 5 L4.3 10 M10.5 5 L13.7 10 M5.2 12.5 H12.8" stroke="#333" stroke-width="1.2"/></svg>
  </div>
</div>
<div class="episode-date abs" style="top:663px">Feb 9, 2020</div>
<p class="episode-summary abs" style="top:701px">Testosterone is lower today than it has ever been through all of human history. This is because we're surrounded with chemicals that are actively preventing our body from making testosterone. In this episode, Dale Horvik explains what you're doing to accidentally lower your testosterone and how to make simple changes to...</p>
<div class="read-more abs" style="top:793px">Read More</div>
<div class="episode-rule abs" style="top:841px"></div>

<h2 class="episode-title abs" style="top:867px">The 80/100 Rule - How to Show a Girl You Like Her</h2>
<div class="player abs" style="top:914px">
  <div class="player-art abs">The Steadfast Fellow Hour</div>
  <div class="player-play abs"><svg width="26" height="30" viewBox="0 0 26 30"><path d="M1 0 L26 15 L1 30 Z" fill="#000"/></svg></div>
  <div class="player-show abs">The Steadfast Fellow Hour</div>
  <div class="player-episode abs">The 80/100 Rule - How to Show a Girl You Like Her</div>
  <div class="player-track abs"></div>
</div>
<div class="episode-date abs" style="top:868px">Feb 6, 2020</div>
<p class="episode-summary abs" style="top:906px">Most guys show too much interest in girls when speaking to them. Then, when they first start learning seduction, they calibrate too far in the opposite direction and don't show enough interest. Attraction is all about BALANCE. In this episode, Dale Horvik explains how</p>

</body>
</html>
```